Velvetorchid Hair & Beauty Business Card

Velvetorchid Hair & Beauty is a boutique salon located in the picturesque Lake Rotomere NZ. The salon is very luxurious, opulent gold gilded mirrors, chandelier lit, contemporary french decor, sets the mood to create beautiful hair, makeup and all beauty services. Just had a new logo design and now after a new business card.
Logo
14 Korowhai Street
Rotomere
Phone (07) 548 6193
www.velvetorchid.co.nz
email hair@velvetorchid.co.nz
Marlena Swithin
Also need a space to put in Stylist name, date, appointment time. thanks;)
Another idea is we could incorporate the wallpaper in the back ground either on the back or front or use an ornate glided frame (around the edge of the card) like on my website where my brides photos flash.
Decided against the wall paper but at least you can see our colour theme for the salon.
Updates

Please check out my updated brief . Thanks :)

Target Market(s)

25-60 years plus, mainly mid age females , wanting the best possible service , high standard of workmanship and money not a problem.

Industry/Entity Type

Boutique

Requirements
Must have
• Gold and silver

```html
<!DOCTYPE html>
<html lang="en">
<head>
<meta charset="utf-8">
<title>Velvetorchid Hair &amp; Beauty – Business Card</title>
<link rel="stylesheet" href="https://fonts.googleapis.com/css2?family=Raleway:wght@400;700&family=Cinzel:wght@600&display=swap">
<style>
  :root {
    --backdrop: #e9e6e1;
    --card-white: #f7f7f5;
    --charcoal: #262626;
    --gold: #b4912f;
    --gold-soft: #ddd0a8;
    --silver: #8c8c8c;
    --ink: #2b2b2b;
    --rule: #a9a9a9;
  }
  * { box-sizing: border-box; margin: 0; padding: 0; }
  html, body {
    width: 1200px; height: 900px; overflow: hidden;
    background: var(--backdrop);
  }
  .sheet {
    width: 1200px; height: 900px;
    display: flex; flex-direction: column; align-items: center; justify-content: center;
    gap: 40px;
  }
  .card {
    position: relative;
    width: 700px; height: 400px;
    box-shadow: 0 6px 18px rgba(0,0,0,0.15);
    overflow: hidden;
  }

  /* Front */
  .card-front { background: var(--card-white); }
  .flourish { position: absolute; }
  .flourish-top-left {
    left: 0; top: 0; width: 170px; height: 110px;
    background: radial-gradient(ellipse at top left, var(--gold-soft) 0%, rgba(221,208,168,0.35) 45%, rgba(247,247,245,0) 75%);
  }
  .flourish-bottom-right {
    right: 0; bottom: 0; width: 210px; height: 150px;
    background: radial-gradient(ellipse at bottom right, var(--gold-soft) 0%, rgba(221,208,168,0.35) 45%, rgba(247,247,245,0) 75%);
  }
  .wordmark {
    display: flex; align-items: center; gap: 12px;
    font-family: 'Raleway', sans-serif; font-weight: 400;
    font-size: 24px; letter-spacing: 0.5px; color: var(--silver);
    white-space: nowrap;
  }
  .wordmark-dot {
    width: 12px; height: 12px; border-radius: 50%; background: var(--gold); flex: none;
  }
  .card-front .wordmark { position: absolute; left: 60px; top: 118px; }

  .contact {
    position: absolute; left: 330px; top: 205px;
    font-family: 'Raleway', sans-serif; color: var(--ink);
  }
  .contact-name {
    font-weight: 700; font-size: 17px; letter-spacing: 1.5px; margin-bottom: 22px;
  }
  .contact-address { font-size: 12px; line-height: 20px; letter-spacing: 0.8px; margin-bottom: 12px; }
  .contact-list { list-style: none; }
  .contact-list li {
    display: flex; align-items: center; gap: 14px;
    font-size: 12px; letter-spacing: 0.8px; line-height: 22px;
  }
  .contact-list svg { width: 13px; height: 13px; fill: var(--gold); }

  /* Back */
  .card-back { background: var(--charcoal); }
  .damask {
    position: absolute; inset: 0;
    background: radial-gradient(ellipse at 50% 30%, #323232 0%, var(--charcoal) 70%);
  }
  .card-back .wordmark {
    position: absolute; left: 0; right: 0; top: 96px; justify-content: center; font-size: 26px;
  }
  .appointment {
    position: absolute; left: 0; right: 0; top: 220px; height: 130px;
    background: var(--card-white);
    padding: 24px 0 0 170px;
  }
  .appointment-row {
    display: flex; align-items: flex-end; gap: 16px; height: 28px;
    font-family: 'Cinzel', serif; font-weight: 600; font-size: 13px; letter-spacing: 3px; color: var(--gold);
  }
  .appointment-row .label { width: 90px; }
  .appointment-row .line { width: 300px; height: 1px; background: var(--rule); margin-bottom: 5px; }
</style>
</head>
<body>
<main class="sheet">

  <section class="card card-front" aria-label="Business card front">
    <div class="flourish flourish-top-left" role="img" aria-label="Gold filigree scroll ornament in corner"></div>
    <div class="flourish flourish-bottom-right" role="img" aria-label="Gold filigree scroll ornament in corner"></div>

    <div class="wordmark"><span class="wordmark-dot"></span>Velvetorchid Hair &amp; Beauty</div>

    <div class="contact">
      <p class="contact-name">Marlena Swithin</p>
      <p class="contact-address">14 Korowhai Street<br>Rotomere</p>
      <ul class="contact-list">
        <li>
          <svg viewBox="0 0 16 16" aria-hidden="true"><path d="M3 1h3l1.5 4-2 1.2a9 9 0 0 0 4.3 4.3L11 8.5 15 10v3a2 2 0 0 1-2 2A12 12 0 0 1 1 3a2 2 0 0 1 2-2z"/></svg>
          (07) 548 6193
        </li>
        <li>
          <svg viewBox="0 0 16 16" aria-hidden="true"><path d="M1 3h14v10H1z M2 4.2v.4l6 4 6-4v-.4z" fill-rule="evenodd"/></svg>
          hair@velvetorchid.co.nz
        </li>
        <li>
          <svg viewBox="0 0 16 16" aria-hidden="true"><path d="M8 1a7 7 0 1 0 0 14A7 7 0 0 0 8 1zm0 1.5a5.5 5.5 0 1 1 0 11 5.5 5.5 0 0 1 0-11zM4 7.2h8v1.6H4z"/></svg>
          www.velvetorchid.co.nz
        </li>
      </ul>
    </div>
  </section>

  <section class="card card-back" aria-label="Business card back">
    <div class="damask" role="img" aria-label="Subtle dark charcoal damask wallpaper pattern"></div>
    <div class="wordmark"><span class="wordmark-dot"></span>Velvetorchid Hair &amp; Beauty</div>
    <div class="appointment">
      <div class="appointment-row"><span class="label">Stylist</span><span class="line"></span></div>
      <div class="appointment-row"><span class="label">Date</span><span class="line"></span></div>
      <div class="appointment-row"><span class="label">Time</span><span class="line"></span></div>
    </div>
  </section>

</main>
</body>
</html>
```